Sophisticated, clean website reflecting my feminine, playful side to sell my abstract art,

I need a website no more than 3 pages to showcase my paintings, a little about me and some contact info. I do abstracts so looking for something a little edgy, yet feminine and current.
Updates

Hi there, These are some artists websites that I Iike: Mirabelvoss.com (I like how airy it is) tobiasmerrowind.com kevinplodderas.com (I like how it scrolls) I'll need a place for a photo ( a headshot-i do not have it yet so I'll need to be able to upload that later) as well as an area for my bio. Also, it's important that I will be able to upload any new photos and descriptions easily so it should be user friendly. Lastly, I like in a sunny place so would like to have this seem upbeat and playful as that is how i like to paint. thanks-I'm trying to upload my photos now -

Target Market(s)

ppl ages 35-70 who want large scale art for their homes

Industry/Entity Type

art

Coding

Coded - Design and coding required

Number of Pages Required

3 page

Colors

Designer to choose colors to be used in the design.

Requirements
Must have
• photos of my art, a place for my bio, be easy to reach me. tasteful-nothing too "in your face" -my clients are pretty high end and organized. They like clean lines
Nice to have
• sophisticated background, muted tones in the back-similar clean font throughout-no cursive
Should not have
• too many dark areas. Too many blocks of color. Too serious.

```html
<!DOCTYPE html>
<html lang="en">
<head>
<meta charset="utf-8">
<title>Celeste Marlowe — Art Gallery</title>
<link href="https://fonts.googleapis.com/css2?family=Playfair+Display:wght@400;600&family=Source+Sans+3:wght@400;600&display=swap" rel="stylesheet">
<style>
:root{
  --ink:#1c1c1c;
  --muted:#555;
  --line:#c9c9c9;
  --frame:#a8a8a8;
  --band:#efefef;
  --paper:#ffffff;
}
*{box-sizing:border-box;margin:0;padding:0}
html,body{width:1200px;height:4032px;overflow:hidden;background:var(--paper);color:var(--ink);font-family:"Source Sans 3",sans-serif}
.page{position:relative;width:1200px;height:4032px}
.abs{position:absolute}
.serif{font-family:"Playfair Display",serif;font-weight:400}
.circle-icon{position:absolute;width:30px;height:30px;border:1.5px solid var(--ink);border-radius:50%;display:flex;align-items:center;justify-content:center;font-size:12px;font-weight:600}
.circle-icon svg{width:14px;height:14px}
.btn{position:absolute;border:1.5px solid var(--ink);background:var(--paper);display:flex;align-items:center;justify-content:center;font-size:14px;font-weight:600}
.brand-title{left:0;width:1200px;top:22px;text-align:center;font-size:33px;font-weight:600;font-family:"Playfair Display",serif}
.nav{left:0;width:1200px;top:84px;display:flex;justify-content:center;gap:26px;font-size:11px;font-weight:600}
.nav .active{text-decoration:underline}
.hero{left:0;top:130px;width:1200px;height:499px;background:linear-gradient(100deg,#8a6a48 0 7%,#e8efe6 7% 14%,#2f9a6e 22%,#6fb34a 45%,#3e8c3a 60%,#c8b86a 72%,#5aa04a 85%,#2f6e4e 100%)}
.hero-title{left:0;width:1200px;top:265px;text-align:center;font-size:62px;font-weight:600;color:#fff}
.dots{left:555px;top:592px;display:flex;gap:8px}
.dots span{width:13px;height:13px;border-radius:50%;background:#555}
.dots span.on{background:#111}
.h2{font-size:50px}
.body-text{font-size:13.5px;line-height:22.4px;color:#333}
.field{position:absolute;border-bottom:1.5px solid var(--line);font-size:13px;padding-bottom:8px;height:22px}
.insta{position:absolute;top:2962px;width:240px;height:208px}
.foot-h{font-size:22px}
.foot-link{font-size:13px;color:#444;position:absolute}
</style>
</head>
<body>
<div class="page">

  <!-- header -->
  <div class="circle-icon" style="left:102px;top:26px">S</div>
  <div class="circle-icon" style="left:145px;top:26px">L</div>
  <div class="circle-icon" style="left:189px;top:26px">F</div>
  <div class="circle-icon" style="left:233px;top:26px"><svg viewBox="0 0 16 16" fill="none" stroke="#1c1c1c" stroke-width="1.4"><rect x="2" y="4" width="12" height="8"/><path d="M2 4l6 5 6-5"/></svg></div>
  <div class="circle-icon" style="left:277px;top:26px"><svg viewBox="0 0 16 16" fill="none" stroke="#1c1c1c" stroke-width="1.4"><path d="M4 2l3 3-2 2c1 2 2 3 4 4l2-2 3 3-2 2C7 14 2 9 2 4z"/></svg></div>
  <div class="abs brand-title">Celeste Marlowe</div>
  <div class="circle-icon" style="left:824px;top:26px"><svg viewBox="0 0 16 16" fill="#1c1c1c"><circle cx="8" cy="5.5" r="3"/><path d="M2.5 14c0-3.5 2.5-5 5.5-5s5.5 1.5 5.5 5z"/></svg></div>
  <div class="circle-icon" style="left:868px;top:26px"><svg viewBox="0 0 16 16" fill="none" stroke="#1c1c1c" stroke-width="1.4"><path d="M8 14S2 10 2 6a3 3 0 016-1 3 3 0 016 1c0 4-6 8-6 8z"/></svg></div>
  <div class="circle-icon" style="left:912px;top:26px"><svg viewBox="0 0 16 16" fill="none" stroke="#1c1c1c" stroke-width="1.4"><path d="M1 2h2l2 8h8l2-6H4"/><circle cx="6" cy="13" r="1"/><circle cx="12" cy="13" r="1"/></svg></div>
  <div class="btn" style="left:973px;top:16px;width:125px;height:50px">Login</div>
  <nav class="abs nav"><span class="active">Home</span><span>Reviews</span><span>Art Gallery</span><span>Collection</span><span>About The Artist</span><span>Contact</span></nav>

  <!-- hero -->
  <div class="abs hero" role="img" aria-label="Close-up of a green and teal abstract painting on a wooden wall"></div>
  <div class="abs hero-title serif" style="font-weight:600">Welcome To My Art Gallery</div>
  <div class="btn" style="left:505px;top:372px;width:188px;height:50px;border-color:#fff">Explore All</div>
  <div class="abs dots"><span></span><span class="on"></span><span></span></div>

  <!-- about -->
  <div class="abs" style="left:86px;top:724px;width:477px;height:481px;background:var(--frame);transform:rotate(1deg)"></div>
  <div class="abs" style="left:96px;top:732px;width:460px;height:468px;background:#fff"></div>
  <div class="abs" role="img" aria-label="Portrait photo of the artist" style="left:102px;top:738px;width:446px;height:456px;background:linear-gradient(160deg,#5a5036,#3a3424 50%,#2a2a26)"></div>
  <h2 class="abs serif h2" style="left:638px;top:742px">About The Artist</h2>
  <p class="abs body-text" style="left:638px;top:868px;width:462px">Lorem ipsum dolor sit amet, consectetur adipiscing elit. Consequat quis turpis adipiscing tincidunt. Fames ut lectus tempus quis lacus nunc arcu. Mi, ultrices varius ultrices massa aliquam odio enim quam. Quisque libero sed eget pellentesque imperdiet. At et lorem habitant amet morbi velit, sed eu lorem. Egestas egestas mattis ultrices aliquam. Malesuada at malesuada convallis feugiat. Pharetra venenatis odio duis quis semper amet. Amet justo, enim ac lacus, aenean elementum. Commodo fermentum viverra consectetur at elit mauris a orci. Quis molestie cursus nisi lorem mi.<br>Suscipit cursus sagittis odio ut sit in aliquam at amet. Leo orci sed mauris sit morbi mi diam vestibulum. Ultrices aliquam donec semper gravida nibh dictum dui. Suspendisse ultrices egestas dui a, faucibus. Eget a id placerat semper consectetur. Integer augue tortor etiam quis. Euismod imperdiet elit proin fames felis lectus justo.</p>

  <!-- gallery -->
  <h2 class="abs serif h2" style="left:0;width:1200px;text-align:center;top:1302px">Art Gallery</h2>
  <div class="abs" style="left:0;top:1425px;width:1200px;height:742px;border-top:1.5px solid var(--line);border-bottom:1.5px solid var(--line)"></div>
  <div class="abs" style="left:600px;top:1425px;width:1.5px;height:742px;background:var(--line)"></div>
  <div class="abs" role="img" aria-label="Abstract painting with blue, yellow and rust swirls" style="left:103px;top:1510px;width:432px;height:574px;background:linear-gradient(90deg,#e9e4d6 0 78%,#a8865e 78%)"></div>
  <div class="abs" role="img" aria-label="Next abstract painting in warm tones" style="left:1101px;top:1522px;width:99px;height:499px;background:linear-gradient(160deg,#c89a6a,#e6d2a8 50%,#b8a8b8)"></div>
  <svg class="abs" style="left:46px;top:1787px" width="14" height="18" viewBox="0 0 14 18"><path d="M10 2L3 9l7 7" fill="none" stroke="#1c1c1c" stroke-width="2.5"/></svg>
  <svg class="abs" style="left:1140px;top:1787px" width="14" height="18" viewBox="0 0 14 18"><path d="M4 2l7 7-7 7" fill="none" stroke="#1c1c1c" stroke-width="2.5"/></svg>
  <h3 class="abs serif" style="left:665px;top:1660px;font-size:43px;line-height:53px">Name Of The<br>Painting</h3>
  <p class="abs body-text" style="left:665px;top:1798px;width:330px">Lorem ipsum dolor sit amet, consectetur adipiscing elit. Consequat quis turpis adipiscing tincidunt. Fames ut lectus tempus quis lacus nunc arcu. Mi, ultrices varius ultrices massa aliquam odio enim quam. Quisque libero sed eget pellentesque imperdiet. At et lorem habitant amet morbi velit,</p>

  <!-- contact form -->
  <h2 class="abs serif h2" style="left:160px;width:500px;text-align:center;top:2260px">Say Hello!</h2>
  <div class="field" style="left:153px;top:2389px;width:204px">First Name</div>
  <div class="field" style="left:463px;top:2389px;width:203px">Last Name</div>
  <div class="field" style="left:153px;top:2454px;width:513px">Email Address</div>
  <div class="field" style="left:153px;top:2520px;width:513px">Message</div>
  <div class="btn" style="left:153px;top:2600px;width:188px;height:50px">Send</div>
  <div class="abs" style="left:843px;top:2312px;width:255px;height:287px;border:1.5px solid var(--line);display:flex;align-items:center;justify-content:center;font-family:'Playfair Display',serif;font-size:28px;font-weight:600">Celeste Marlowe</div>
  <div class="abs" style="left:0;top:2744px;width:1200px;height:1.5px;background:var(--line)"></div>

  <!-- social feed -->
  <h2 class="abs serif h2" style="left:0;width:1200px;text-align:center;top:2838px">Follow Me On Snapwall</h2>
  <div class="insta" style="left:102px;background:linear-gradient(135deg,#e6e0ec,#6e58a8 50%,#d8cce0)" role="img" aria-label="Purple abstract painting detail"></div>
  <div class="insta" style="left:354px;background:linear-gradient(135deg,#b04a30,#e8d0c0 50%,#9a3a24)" role="img" aria-label="Rust red abstract painting detail"></div>
  <div class="insta" style="left:605px;background:linear-gradient(135deg,#6a4a48,#d8a0a8 50%,#c08a90)" role="img" aria-label="Pink floral abstract painting detail"></div>
  <div class="insta" style="left:857px;width:241px;background:linear-gradient(135deg,#d8a8b0,#b07880 50%,#e6c4c8)" role="img" aria-label="Pink swirl abstract painting detail"></div>
  <div class="btn" style="left:505px;top:3232px;width:188px;height:50px">Follow</div>

  <!-- newsletter -->
  <div class="abs" style="left:0;top:3376px;width:1200px;height:230px;background:var(--band)"></div>
  <h2 class="abs serif h2" style="left:0;width:1200px;text-align:center;top:3408px">Get In Touch</h2>
  <div class="abs" style="left:227px;top:3500px;width:745px;height:75px;background:#fff"></div>
  <div class="abs" style="left:258px;top:3530px;font-size:11px">Email Address</div>
  <div class="btn" style="left:754px;top:3512px;width:186px;height:50px">Sign Up</div>

  <!-- footer -->
  <div class="abs serif" style="left:99px;top:3770px;font-size:30px;font-weight:600">Celeste Marlowe</div>
  <div class="abs serif foot-h" style="left:429px;top:3700px">Quick Links</div>
  <div class="foot-link" style="left:429px;top:3762px">Home</div>
  <div class="foot-link" style="left:429px;top:3793px">Featured Collection</div>
  <div class="foot-link" style="left:429px;top:3825px">Reviews</div>
  <div class="foot-link" style="left:429px;top:3856px">Art Gallery</div>
  <div class="foot-link" style="left:429px;top:3887px">About The Artist</div>
  <div class="abs serif foot-h" style="left:657px;top:3700px">Contact Info</div>
  <div class="circle-icon" style="left:657px;top:3762px"><svg viewBox="0 0 16 16" fill="none" stroke="#1c1c1c" stroke-width="1.4"><path d="M4 2l3 3-2 2c1 2 2 3 4 4l2-2 3 3-2 2C7 14 2 9 2 4z"/></svg></div>
  <div class="foot-link" style="left:708px;top:3769px">000.000.0000</div>
  <div class="circle-icon" style="left:657px;top:3806px"><svg viewBox="0 0 16 16" fill="#1c1c1c"><path d="M8 1a5 5 0 015 5c0 4-5 9-5 9S3 10 3 6a5 5 0 015-5z"/><circle cx="8" cy="6" r="1.8" fill="#fff"/></svg></div>
  <div class="foot-link" style="left:708px;top:3813px">gfgfsgfgddhgjhytrtshgjhfd</div>
  <div class="circle-icon" style="left:657px;top:3850px"><svg viewBox="0 0 16 16" fill="none" stroke="#1c1c1c" stroke-width="1.4"><rect x="2" y="4" width="12" height="8"/><path d="M2 4l6 5 6-5"/></svg></div>
  <div class="foot-link" style="left:708px;top:3857px">hello@celestemarlowe.art</div>
  <div class="abs serif foot-h" style="left:900px;width:198px;text-align:right;top:3700px">Social Links</div>
  <div class="circle-icon" style="left:977px;top:3762px">S</div>
  <div class="circle-icon" style="left:1021px;top:3762px">L</div>
  <div class="circle-icon" style="left:1065px;top:3762px">F</div>
  <div class="abs" style="left:103px;top:3987px;font-size:10px">Terms Of Use</div>
  <div class="abs" style="left:196px;top:3987px;font-size:10px">Privacy Policy</div>
  <div class="abs" style="left:700px;width:398px;text-align:right;top:3987px;font-size:10px">© 2022 Art Gallery. ALL RIGHTS RESERVED</div>

</div>
</body>
</html>
```